Powerpoint template and intro presentation

I have a short presentation of 6 slides that I'd like to be made pretty, see attached below - called target companies Intro.

I'd also like a template incorporating my logo which I have attached below as well

I've attached a jpeg with the logo with white background that is the logo that I would like to incorporate.

Powerpoint and logo file has been uploaded

```html
<!DOCTYPE html>
<html lang="en">
<head>
<meta charset="utf-8">
<title>Smart Art 1 – Slide 12</title>
<link rel="stylesheet" href="https://fonts.googleapis.com/css2?family=Questrial&display=swap">
<style>
  :root {
    --page: #ffffff;
    --green-title: #8cc63f;
    --green-rule: #cde6b0;
    --grey-rule: #cfcfcf;
    --heading-grey: #58585a;
    --box-1: #8cc43f;
    --box-2: #9bcb58;
    --box-3: #a4d166;
    --box-4: #b8da86;
    --box-5: #c4e09d;
    --connector-1: #8cc43f;
    --connector-2: #b8da86;
    --circle-dark: #545458;
    --circle-mid: #78787c;
    --circle-large: #a6a6a9;
    --plus: #414245;
    --chevron: #c3c3c5;
    --text-light: #ffffff;
  }
  * { margin: 0; padding: 0; box-sizing: border-box; }
  html, body { width: 1200px; height: 1000px; overflow: hidden; }
  body {
    background: var(--page);
    font-family: "Questrial", "Century Gothic", sans-serif;
    position: relative;
  }
  .brand {
    position: absolute; left: 88px; top: 128px; width: 160px;
    display: flex; flex-direction: column; align-items: center; gap: 8px;
    color: var(--green-title); font-size: 15px; letter-spacing: 1px; line-height: 1.2;
    text-align: center;
  }
  .brand-dot { width: 18px; height: 18px; border-radius: 50%; background: var(--green-title); }
  .slide-title {
    position: absolute; left: 263px; top: 136px;
    font-size: 41px; font-weight: 400; color: var(--green-title); letter-spacing: 1.5px;
  }
  .rule { position: absolute; }
  .rule-green-top { left: 263px; top: 187px; width: 905px; height: 6px; background: var(--green-rule); }
  .rule-grey-top { left: 263px; top: 198px; width: 905px; height: 2px; background: var(--grey-rule); }
  .rule-green-bottom { left: 33px; top: 862px; width: 1024px; height: 6px; background: var(--green-rule); }
  .rule-grey-bottom { left: 33px; top: 873px; width: 1030px; height: 2px; background: var(--grey-rule); }
  .section-heading {
    position: absolute; top: 239px; width: 520px; text-align: center;
    font-size: 30px; color: var(--heading-grey); letter-spacing: 1.5px; font-weight: 400;
  }
  .heading-list { left: 80px; }
  .heading-process { left: 600px; }
  .list-box {
    position: absolute; width: 221px; height: 131px;
    display: flex; align-items: center; justify-content: center; text-align: center;
    color: var(--text-light); font-size: 38px; line-height: 1.1;
  }
  .list-box.b1 { left: 92px; top: 302px; background: var(--box-1); }
  .list-box.b2 { left: 369px; top: 302px; background: var(--box-2); }
  .list-box.b3 { left: 92px; top: 489px; background: var(--box-3); }
  .list-box.b4 { left: 369px; top: 489px; background: var(--box-4); }
  .list-box.b5 { left: 92px; top: 676px; background: var(--box-5); }
  .diagram-lines { position: absolute; left: 0; top: 0; }
  .process-circle {
    position: absolute; border-radius: 50%;
    display: flex; align-items: center; justify-content: center; text-align: center;
    color: var(--text-light); line-height: 1.1;
  }
  .circle-input-a { left: 612px; top: 365px; width: 136px; height: 136px; background: var(--circle-dark); font-size: 23px; }
  .circle-input-b { left: 612px; top: 608px; width: 136px; height: 136px; background: var(--circle-mid); font-size: 23px; }
  .circle-result { left: 835px; top: 416px; width: 276px; height: 276px; background: var(--circle-large); font-size: 48px; }
  .page-number {
    position: absolute; left: 1070px; top: 857px; width: 42px; height: 42px; border-radius: 50%;
    background: var(--green-title); color: var(--text-light);
    display: flex; align-items: center; justify-content: center; font-size: 17px;
  }
</style>
</head>
<body>
  <div class="brand"><span class="brand-dot"></span><span class="brand-name">MERIDIAN<br>DATA SYSTEMS</span></div>
  <h1 class="slide-title">Smart Art 1</h1>
  <div class="rule rule-green-top"></div>
  <div class="rule rule-grey-top"></div>

  <h2 class="section-heading heading-list">Smart Art List in Green</h2>
  <h2 class="section-heading heading-process">Smart Art Process in Grey</h2>

  <svg class="diagram-lines" width="1200" height="1000" viewBox="0 0 1200 1000" aria-hidden="true">
    <g fill="none" stroke-width="1.6">
      <g stroke="var(--connector-1)">
        <path d="M318 368 H361 M354 362 L361 368 L354 374"/>
        <path d="M480 436 V461 H203 V481 M197 474 L203 481 L209 474"/>
      </g>
      <g stroke="var(--connector-2)">
        <path d="M318 555 H361 M354 549 L361 555 L354 561"/>
        <path d="M480 624 V648 H203 V667 M197 660 L203 667 L209 660"/>
      </g>
    </g>
    <path class="plus-sign" fill="var(--plus)" d="M670 526 H690 V545 H710 V565 H690 V584 H670 V565 H650 V545 H670 Z"/>
    <path class="process-arrow" fill="var(--chevron)" d="M771 541 H793 V530 L815 555 L793 580 V569 H771 Z"/>
  </svg>

  <div class="list-box b1">Sample<br>Text</div>
  <div class="list-box b2">Sample<br>Text</div>
  <div class="list-box b3">Sample<br>Text</div>
  <div class="list-box b4">Sample<br>Text</div>
  <div class="list-box b5">Sample<br>Text</div>

  <div class="process-circle circle-input-a">Sample<br>Text</div>
  <div class="process-circle circle-input-b">Sample<br>Text</div>
  <div class="process-circle circle-result">Sample<br>Text</div>

  <div class="rule rule-green-bottom"></div>
  <div class="rule rule-grey-bottom"></div>
  <div class="page-number">12</div>
</body>
</html>
```